Book and Ebook Cover for my Upcoming Book

About the Book
------------------
I need a book, ebook and if possible audio cover design for my upcoming book - Lanterns & Larkspur. This is my first book and really looking for a great book cover. The book is about my story, living with Mental Health and how to reclaim control of your life.

Quillbarrow
-----------
I am using quillbarrow.com to self-publish my book so in case of any design-related questions you can just search info on their website.

I have an initial theme I am thinking for the design book cover which I have attached. You can use this as a starting point.

Idea for the theme
---------------------
I am thinking about a phoenix to represent rising from the ashes and rebirth. The phoenix motif will be continued throughout the interior pages of the book. I'd like the cover of the book to be minimal, white with gold lettering, and maybe incorporating wings? feel free to play around with the idea and up for suggestions.

If you can think of something along these lines and make it a lot better that would be great.

What I need
---------------
The book is complete and is Trim size is 6.14 x 9.21” (234 x 156mm). I would need-
1. Book Cover
2. Back & Spine Design
3. Source File
4. Ebook Cover
5. Need multiple revisions to get the best possible outcome
6. My name and book title should also on the front cover
7. The book title should be bigger size than the subtitle

If you can give me Audiobook cover, I would love that as well and can pay extra for it if needed.

I love this for the interior phoenix motif:
https://craftbazaarly.com/InkMoth/7720458-Watercolor-Heron-Clipart-Set#fullscreen

The only other actual book cover I found online that remotely relates to what I am looking for is this -
https://www.lookfinder.example/url?sa=i&url=https%3A%2F%2Fpixelmoor.com%2Fvantrell&psig=QxTrPLm3KZ9vBwE2dYcN41HoJuSA&ust=1598415525610000&source=images&cd=vfe&ved=0CAIQjRxqFwoTCPD_toPAtesCFQAAAAAdAAAAABAD

Target Market(s)

Personal Development
Mental health

Requirements
Must have
• 1. Book Cover
2. Back & Spine Design
3. Source File
4. Ebook Cover
Nice to have
• Audiobook cover as I eventually will be releasing the audio version of the book

```html
<!DOCTYPE html>
<html lang="en">
<head>
<meta charset="utf-8">
<title>Lanterns &amp; Larkspur — Print Cover Spread</title>
<link rel="stylesheet" href="https://fonts.googleapis.com/css2?family=Cormorant+Garamond:ital,wght@0,500;1,500;1,600&family=Cinzel:wght@500;600&family=Great+Vibes&family=Lato:wght@400;700&display=swap">
<style>
  :root {
    --page: #ffffff;
    --silver-edge: #bdbdbd;
    --silver-mid: #dcdcdc;
    --silver-light: #ffffff;
    --ink: #141414;
    --gold-dark: #9a6a12;
    --gold: #d9a93a;
    --gold-light: #f6dc8a;
    --feather-rose: #c9826a;
    --feather-amber: #c99a4a;
    --feather-cream: #f3e3d2;
  }
  * { margin: 0; padding: 0; box-sizing: border-box; }
  html, body { width: 1200px; height: 800px; overflow: hidden; background: var(--page); }
  .spread { position: relative; width: 1200px; height: 800px; background: var(--page); }

  .panel {
    position: absolute; top: 0; height: 800px;
    background: linear-gradient(90deg, var(--silver-edge) 0%, var(--silver-mid) 22%, var(--silver-light) 48%, var(--silver-light) 54%, var(--silver-mid) 78%, var(--silver-edge) 100%);
  }
  .back-cover { left: 45px; width: 533px; }
  .front-cover { left: 622px; width: 533px; }
  .spine { position: absolute; left: 578px; top: 0; width: 44px; height: 800px; background: var(--page); }

  .art {
    position: absolute;
    background: radial-gradient(ellipse at 50% 60%, var(--feather-cream) 0%, var(--feather-rose) 45%, var(--feather-amber) 75%, transparent 100%);
    opacity: 0.85;
  }
  .back-cover .wing-emblem { left: 220px; top: 30px; width: 96px; height: 76px; border-radius: 50% 50% 40% 40%; }
  .front-cover .wing-emblem { left: 222px; top: 30px; width: 96px; height: 76px; border-radius: 50% 50% 40% 40%; }
  .feather-wings { left: 58px; top: 315px; width: 430px; height: 375px; border-radius: 50% 50% 45% 45% / 40% 40% 60% 60%; opacity: 0.7; }

  .back-heading {
    position: absolute; left: 0; width: 533px; top: 100px; text-align: center;
    font-family: "Cormorant Garamond", serif; font-style: italic; font-weight: 500;
    font-size: 50px; color: var(--ink); letter-spacing: 1px; line-height: 1;
  }
  .back-heading .connector { font-family: "Great Vibes", cursive; font-style: normal; font-size: 44px; margin: 0 -4px; }
  .back-subtitle {
    position: absolute; left: 0; width: 533px; top: 178px; text-align: center;
    font-family: "Lato", sans-serif; font-weight: 700; font-size: 19px; color: var(--ink);
  }
  .blurb {
    position: absolute; left: 43px; width: 452px;
    font-family: "Lato", sans-serif; font-size: 13.4px; line-height: 17.6px; color: var(--ink);
  }
  .blurb-1 { top: 234px; } .blurb-2 { top: 319px; } .blurb-3 { top: 405px; } .blurb-4 { top: 514px; }

  .spine-title, .spine-author {
    position: absolute; left: 0; width: 44px; writing-mode: vertical-rl;
    display: flex; align-items: center; color: var(--ink);
  }
  .spine-title {
    top: 96px; font-family: "Cormorant Garamond", serif; font-style: italic; font-weight: 500;
    font-size: 27px; letter-spacing: 1px; white-space: nowrap;
  }
  .spine-author {
    top: 528px; font-family: "Cormorant Garamond", serif; font-style: italic; font-weight: 500;
    font-size: 25px; letter-spacing: 1px; white-space: nowrap;
  }

  .gold {
    background: linear-gradient(180deg, var(--gold-light) 0%, var(--gold) 45%, var(--gold-dark) 70%, var(--gold) 100%);
    -webkit-background-clip: text; background-clip: text; color: transparent;
  }
  .front-title {
    position: absolute; left: 0; width: 533px; top: 112px; text-align: center;
    font-family: "Cormorant Garamond", serif; font-style: italic; font-weight: 600;
    font-size: 80px; line-height: 72px; letter-spacing: 2px;
  }
  .front-title .amp { display: block; font-size: 72px; }
  .front-author {
    position: absolute; left: 0; width: 533px; top: 727px; text-align: center;
    font-family: "Cinzel", serif; font-weight: 600; font-size: 25px; letter-spacing: 1px;
  }
</style>
</head>
<body>
<main class="spread">
  <section class="panel back-cover">
    <div class="art wing-emblem" role="img" aria-label="Small pair of watercolour wings emblem"></div>
    <h2 class="back-heading">A STORY <span class="connector">of</span> HOPE</h2>
    <p class="back-subtitle">When Struggle Leads to Empowerment</p>
    <p class="blurb blurb-1">Lorem ipsum dolor sit amet, consectetur adipiscing elit, sed do eiusmod tempor incididunt ut labore et dolore magna aliqua. Quis ipsum suspendisse ultrices gravida. Risus commodo viverra maecenas accumsan lacus vel facilisis.</p>
    <p class="blurb blurb-2">Lorem ipsum dolor sit amet, consectetur adipiscing elit, sed do eiusmod tempor incididunt ut labore et dolore magna aliqua. Quis ipsum suspendisse ultrices gravida. Risus commodo viverra maecenas accumsan lacus vel facilisis.</p>
    <p class="blurb blurb-3">Lorem ipsum dolor sit amet, consectetur adipiscing elit, sed do eiusmod tempor incididunt ut labore et dolore magna aliqua. Quis ipsum suspendisse ultrices gravida. Risus commodo viverra maecenas accumsan lacus vel facilisis.</p>
    <p class="blurb blurb-4">Lorem ipsum dolor sit amet, consectetur adipiscing elit, sed do eiusmod tempor incididunt ut labore et dolore magna aliqua. Quis ipsum suspendisse ultrices gravida. Risus commodo viverra maecenas accumsan lacus vel facilisis.</p>
  </section>

  <section class="spine">
    <p class="spine-title">LANTERNS &amp; LARKSPUR</p>
    <p class="spine-author">MERIVEL TK</p>
  </section>

  <section class="panel front-cover">
    <div class="art wing-emblem" role="img" aria-label="Small pair of watercolour wings emblem"></div>
    <h1 class="front-title gold">LANTERNS<span class="amp">&amp;</span>LARKSPUR</h1>
    <div class="art feather-wings" role="img" aria-label="Large watercolour phoenix feathers fanned out as a pair of wings, crossing at the base"></div>
    <p class="front-author gold">MERIVEL TK</p>
  </section>
</main>
</body>
</html>
```